Amazing Homepage required for Ireland's Top Crowdfunding site

Design/ PSD Files required.

BrookLedger.com is the market leader in crowd lending/peer to peer lending in Ireland. Businesses/SME’s can borrow anything from €5,000 to €100,000 at interest rates much more favourable than those offered by the banks. BL is also a quicker and less bureaucratic than traditional lending institutions. We are a viable alternative to banks and traditional sources of finance.

Our lenders are members of the public and they can lend directly to Irish businesses in amounts from €50 to €2,000. They get a better rate of return than deposit accounts, as well as the feel good factor of supporting a local business.

We have just completed a full rebrand of our logo and colours and would now like to utilise these to best effect by implementing them in a total redesign of our homepage to attract borrowers and lenders. Please see the attached files for the brand guidelines and logo/colours to be used.

We are looking for a designer to utilise our new branding in a creative way, conveying that we are modern, trustworthy, competitive and friendly/local.

We currently have two different user groups:
1- Lenders; this currently consists of members of the public but in future will expand to include financial institutions

2- Business borrowers looking for funds for their business

Embracing and balancing both of these user groups is difficult so we would like the homepage to primarily target borrowers but incorporate clear alternative calls to action for lenders/prospective lenders as well.

We would like:
Infinite scroll homepage
New logo and tagline on a fixed header which should also include; ‘Marketplace’ ‘About’ ‘FAQ’ and a clear login button
A static full bleed image
Overlaid over this we would like a loan calculator in a similar style/functionality to this one on www.pelvaro.com. It should have:
an image of a slider icon with amounts from €0 to €100,000
A text field with ‘Business Loan amount’ which fills when the slider is moved
Then, a text field called ‘Monthly repayment’
An email field with a clear call to action ie ‘Go’ or ‘Get Started’
The purpose of this is to enable prospective borrowers to quickly and easily get a quote estimate for their loan
Underneath this we would like to have an alternate call to action to target prospective lenders; something like ‘Looking to Lend?’

Further down the page we would like to have a heading ‘What is Brook Ledger?’
(include information from company overview)

3 images to illustrate loans live in our Marketplace

Target Market(s)

This Homepge should appeal to small business owners

Industry/Entity Type

Crowd

Number of Pages Required

1 page

Font styles to use
Sans Serif

Requirements
Must have
• Linear clean and modern homepage
• Clear calls to action
Nice to have
• Ideas for how video/rich media might be incorporated into a future iteration of the homepage

```html
<!DOCTYPE html>
<html lang="en">
<head>
<meta charset="utf-8">
<title>Brook Ledger – Crowd Lending in Ireland</title>
<link rel="stylesheet" href="https://fonts.googleapis.com/css2?family=Questrial&family=Montserrat:wght@400;600;700&display=swap">
<style>
:root{
  --orange:#e2683c;
  --orange-soft:#d9744f;
  --orange-deep:#b9532f;
  --card:rgba(110,45,22,.42);
  --faq:#c9714f;
  --ink:#222;
  --dark:#141414;
  --grey:#e6e6e6;
  --mid:#6b6b6b;
  --white:#fff;
}
*{box-sizing:border-box;margin:0;padding:0}
html,body{width:1200px;height:3399px;overflow:hidden}
body{position:relative;background:#fff;font-family:"Questrial",sans-serif;color:var(--ink);font-size:14px}
section,header,footer{position:absolute;left:0;width:1200px;overflow:hidden}
.btn{display:inline-block;background:var(--orange);color:#fff;font-family:"Montserrat",sans-serif;font-weight:600;font-size:11px;text-transform:uppercase;padding:8px 14px;letter-spacing:.5px}
.ph{position:absolute}

/* hero */
.hero{top:0;height:440px;background:#2a2d33}
.hero-photo{left:0;top:0;width:1200px;height:440px;background:linear-gradient(180deg,#c9d4dc 0%,#9fb0bd 45%,#6c7780 100%)}
.hero-shade{position:absolute;inset:0}
.topbar{position:absolute;top:0;left:0;width:1200px;height:70px;background:rgba(10,10,10,.85)}
.logo{position:absolute;left:70px;top:28px;display:flex;align-items:center;gap:10px;font-family:"Montserrat",sans-serif;font-weight:700;font-size:22px;color:#fff}
.logo i{width:16px;height:16px;background:var(--orange);display:block}
.nav{position:absolute;left:420px;top:0;display:flex;height:70px}
.nav a{color:#fff;font-family:"Montserrat",sans-serif;font-weight:700;font-size:12px;text-transform:uppercase;padding:0 20px;line-height:70px;text-decoration:none}
.nav a.active{background:var(--orange)}
.signin{position:absolute;right:90px;top:108px;color:var(--orange);font-size:12px;display:flex;gap:14px;align-items:center}
.hero-copy{position:absolute;left:560px;top:150px;width:460px}
.kicker{color:#fff;font-size:12px;letter-spacing:1px;text-transform:uppercase}
.hero-title{color:var(--orange);font-size:44px;line-height:1.05;margin-top:10px;font-weight:400}
.hero-title b{font-family:"Montserrat",sans-serif;font-weight:700}
.lead-form{margin-top:24px;display:flex;flex-direction:column;gap:8px;width:210px}
.lead-form span{display:block;border:1px solid rgba(255,255,255,.6);color:#fff;font-size:11px;padding:6px 8px;background:rgba(0,0,0,.25)}
.lead-form .btn{align-self:flex-start;margin-top:4px}

/* welcome */
.welcome{top:440px;height:460px;background:linear-gradient(180deg,var(--orange) 0%,var(--orange-soft) 100%);text-align:center;color:#fff}
.welcome h1{margin-top:38px;font-size:44px;font-weight:400;letter-spacing:2px;display:inline-block;border-bottom:2px solid #fff;padding:0 80px 4px}
.welcome .sub{font-size:12px;text-transform:uppercase;margin:12px auto 0;width:560px;line-height:1.45}
.cards{display:flex;gap:10px;justify-content:center;margin-top:28px}
.card{width:265px;height:240px;background:var(--card);text-align:left;padding:22px 18px;position:relative}
.card svg.ico{display:block;margin:0 auto 12px}
.card h3{font-family:"Montserrat",sans-serif;font-weight:700;font-size:14px;text-transform:uppercase;text-align:center;margin-bottom:10px}
.card p{font-size:12px;line-height:1.4}
.card .go{position:absolute;right:16px;bottom:14px}

/* marketplace */
.market{top:900px;height:410px;background:#fff}
.market h2{position:absolute;left:62px;top:8px;font-family:"Montserrat",sans-serif;font-weight:700;font-size:20px;text-transform:uppercase;color:#fff;background:var(--orange-soft);padding:4px 10px 4px 0}
.market .for{position:absolute;left:62px;top:48px;font-family:"Montserrat",sans-serif;font-weight:700;font-size:12px;text-transform:uppercase}
.loans{position:absolute;left:62px;top:80px;display:flex;gap:34px}
.loan{width:335px}
.loan .ph{position:relative;height:180px}
.loan h3{color:var(--orange);font-size:13px;text-transform:uppercase;margin:14px 0 8px}
.loan p{font-size:12px;color:var(--mid);line-height:1.45}
.loan .btn{float:right;margin-top:14px}

/* about + faq */
.about{top:1310px;height:550px;background:var(--grey)}
.about-main{position:absolute;left:0;top:0;width:552px;height:550px;padding:30px 0 0 62px}
.about h2{color:var(--orange);font-size:38px;font-weight:400}
.about h4{font-size:24px;font-weight:400;color:var(--ink);margin-top:2px}
.ensure{display:flex;gap:18px;margin-top:20px}
.ensure .ph{position:relative;width:130px;height:150px;flex:none}
.ensure h5{color:var(--orange);font-size:13px;text-transform:uppercase;margin-bottom:6px}
.ensure p{font-size:11px;line-height:1.4;margin-bottom:8px}
.video{position:absolute;left:62px;top:345px;width:470px;height:170px;background:#d0d0d0;display:flex}
.video-info{width:180px;padding:14px;background:#8a8a8a;color:#fff}
.video-info h5{color:var(--orange);font-size:12px;text-transform:uppercase;margin-bottom:6px}
.video-info p{font-size:11px;line-height:1.4;margin-bottom:6px}
.video .ph{position:relative;flex:1}
.faq{position:absolute;left:552px;top:0;width:648px;height:550px;background:var(--faq);color:#fff;padding:30px 40px}
.faq h2{color:#fff;font-size:30px;font-family:"Montserrat",sans-serif;font-weight:600;border-bottom:1px solid rgba(255,255,255,.6);padding-bottom:8px;margin-bottom:12px}
.faq li{list-style:none;font-size:12px;font-style:italic;padding:7px 0 7px 20px;position:relative;border-bottom:1px solid rgba(255,255,255,.15)}
.faq li:before{content:"›";position:absolute;left:2px;top:4px;font-size:16px;font-style:normal}
.faq li small{display:block;font-size:11px;opacity:.85;margin-top:6px;line-height:1.4}

/* lend banner */
.lend{top:1860px;height:280px;text-align:center}
.lend .ph{inset:0;background:linear-gradient(90deg,#4b4f55 0%,#2d3136 50%,#59524c 100%)}
.lend h2{position:relative;margin-top:70px;color:var(--orange);font-size:64px;font-weight:400;letter-spacing:2px}
.lend p{position:relative;color:#fff;font-size:20px;letter-spacing:8px;text-transform:uppercase}
.lend .btn{position:relative;margin-top:20px}
.lend .arr{position:absolute;top:110px}

/* what's new + calculator */
.news{top:2140px;height:820px;background:#fff}
.news .bg{left:0;top:0;width:560px;height:820px;background:linear-gradient(90deg,#f1ede9 0%,#fff 100%)}
.news-list{position:absolute;left:62px;top:110px;width:240px}
.news-list h2{color:var(--orange);font-size:22px;text-transform:uppercase;font-weight:400;border-bottom:1px solid var(--orange);padding-bottom:6px;margin-bottom:20px}
.prog{display:flex;gap:10px;margin-bottom:26px}
.prog b{color:var(--orange);font-size:34px;line-height:1;font-family:"Montserrat",sans-serif}
.prog h3{font-size:13px;text-transform:uppercase;font-weight:400}
.prog p{font-size:11px;color:var(--mid);line-height:1.4;margin-top:4px}
.calc-title{position:absolute;left:310px;width:818px;top:40px;text-align:center;color:var(--orange);font-size:36px;border-bottom:1px solid var(--orange);padding-bottom:10px}
.calc{position:absolute;left:310px;top:110px;width:818px;height:600px;background:var(--orange-soft);padding:60px 60px;color:#fff}
.row{display:flex;align-items:center;gap:30px;margin-bottom:20px}
.row label{font-size:28px;width:320px}
.val{border:1px solid #fff;font-size:13px;padding:8px 12px;width:110px}
.slider{margin:4px 0 40px;height:26px;position:relative}
.slider:before{content:"";position:absolute;left:0;right:120px;top:12px;height:3px;background:#fff}
.slider i{position:absolute;top:4px;width:18px;height:18px;border-radius:50%;background:#fff}
.calc .apply{position:absolute;right:60px;bottom:60px;background:#fff;color:var(--orange);font-family:"Montserrat",sans-serif;font-weight:700;font-size:13px;padding:12px 22px}

/* footer */
.footer{top:2960px;height:439px;background:var(--dark);color:#fff;display:flex;gap:0;padding:90px 0 0 140px}
.col{width:380px}
.col h4{color:var(--orange);font-size:14px;text-transform:uppercase;border-bottom:1px solid var(--orange);display:inline-block;padding-bottom:4px;margin-bottom:14px}
.col li{list-style:none;font-size:13px;margin-bottom:8px;display:flex;align-items:center;gap:8px;text-transform:uppercase}
.col li i{width:12px;height:12px;border-radius:50%;background:var(--orange);display:block}
.col p{font-size:13px;line-height:1.6}
</style>
</head>
<body>

<header class="hero">
  <div class="ph hero-photo" role="img" aria-label="Businessman in a suit seen from behind, facing a city skyline"></div>
  <svg class="hero-shade" width="1200" height="440"><polygon points="520,70 1200,70 1200,440 380,440" fill="rgba(20,22,26,.72)"/></svg>
  <div class="topbar"></div>
  <div class="logo"><i></i>BrookLedger</div>
  <nav class="nav"><a class="active">Home</a><a>Marketplace</a><a>FAQ</a><a>About us</a></nav>
  <div class="signin">Sign in
    <svg width="14" height="14"><circle cx="6" cy="6" r="4.5" fill="none" stroke="#e2683c" stroke-width="2"/><line x1="9.5" y1="9.5" x2="13" y2="13" stroke="#e2683c" stroke-width="2"/></svg></div>
  <div class="hero-copy">
    <p class="kicker">Market leader in crowd lending</p>
    <h1 class="hero-title">The Best Lending<br>in <b>IRELAND</b></h1>
    <div class="lead-form"><span>Full Name</span><span>E-mail</span><span>Phone</span><a class="btn">Get started now!</a></div>
  </div>
</header>

<section class="welcome">
  <h1>WELLCOME</h1>
  <p class="sub">Our lenders are members of the public and they can lend directly to Irish businesses in amounts from €50 to €2,000</p>
  <div class="cards">
    <div class="card">
      <svg class="ico" width="40" height="44"><path d="M6 2h20l10 10v30H6z" fill="none" stroke="#fff" stroke-width="3"/><line x1="12" y1="20" x2="30" y2="20" stroke="#fff" stroke-width="2"/><line x1="12" y1="27" x2="30" y2="27" stroke="#fff" stroke-width="2"/><line x1="12" y1="34" x2="30" y2="34" stroke="#fff" stroke-width="2"/></svg>
      <h3>Our lenders</h3>
      <p>Our lenders are members of the public and they can lend directly to Irish businesses in amounts from €50 to €2,000. They get a better rate of return than deposit accounts, porting a local business.</p>
      <svg class="go" width="18" height="18"><circle cx="9" cy="9" r="8" fill="none" stroke="#fff" stroke-width="1.5"/><path d="M7 5l4 4-4 4" fill="none" stroke="#fff" stroke-width="1.5"/></svg>
    </div>
    <div class="card">
      <svg class="ico" width="48" height="44"><rect x="4" y="30" width="7" height="12" fill="#fff"/><rect x="15" y="24" width="7" height="18" fill="#fff"/><rect x="26" y="18" width="7" height="24" fill="#fff"/><rect x="37" y="10" width="7" height="32" fill="#fff"/><path d="M4 22L20 10l8 5L44 2" fill="none" stroke="#fff" stroke-width="2.5"/></svg>
      <h3>Our lenders</h3>
      <p>Our lenders are members of the public and they can lend directly to Irish businesses in amounts from €50 to €2,000. They get a better rate of return than deposit accounts, porting a local business.</p>
      <svg class="go" width="18" height="18"><circle cx="9" cy="9" r="8" fill="none" stroke="#fff" stroke-width="1.5"/><path d="M7 5l4 4-4 4" fill="none" stroke="#fff" stroke-width="1.5"/></svg>
    </div>
    <div class="card">
      <svg class="ico" width="50" height="44"><ellipse cx="25" cy="24" rx="20" ry="15" fill="#fff"/><rect x="14" y="34" width="6" height="8" fill="#fff"/><rect x="30" y="34" width="6" height="8" fill="#fff"/><rect x="20" y="10" width="10" height="3" fill="#b9532f"/></svg>
      <h3>Our lenders</h3>
      <p>Our lenders are members of the public and they can lend directly to Irish businesses in amounts from €50 to €2,000. They get a better rate of return than deposit accounts, porting a local business.</p>
      <svg class="go" width="18" height="18"><circle cx="9" cy="9" r="8" fill="none" stroke="#fff" stroke-width="1.5"/><path d="M7 5l4 4-4 4" fill="none" stroke="#fff" stroke-width="1.5"/></svg>
    </div>
    <div class="card">
      <svg class="ico" width="44" height="44"><circle cx="22" cy="16" r="12" fill="none" stroke="#fff" stroke-width="3"/><text x="22" y="21" fill="#fff" font-size="14" text-anchor="middle" font-family="Montserrat,sans-serif">£</text><path d="M4 40h10l8-6h10" fill="none" stroke="#fff" stroke-width="3"/></svg>
      <h3>Our lenders</h3>
      <p>Our lenders are members of the public and they can lend directly to Irish businesses in amounts from €50 to €2,000. They get a better rate of return than deposit accounts, porting a local business.</p>
      <svg class="go" width="18" height="18"><circle cx="9" cy="9" r="8" fill="none" stroke="#fff" stroke-width="1.5"/><path d="M7 5l4 4-4 4" fill="none" stroke="#fff" stroke-width="1.5"/></svg>
    </div>
  </div>
</section>

<section class="market">
  <h2>Marketplace</h2>
  <p class="for">Loans for:</p>
  <div class="loans">
    <article class="loan">
      <div class="ph" role="img" aria-label="Older couple sitting together at home" style="background:linear-gradient(135deg,#d8c9b8,#9a8d80)"></div>
      <h3>Annuity loans</h3>
      <p>We do not work for an insurance company, we work for you, we work on your side when you have a loss and follow through to see that you get often prompt payment. We represent a carefully selected group of reputable insurance companies.</p>
      <a class="btn">Read more</a>
    </article>
    <article class="loan">
      <div class="ph" role="img" aria-label="Smiling man in the driver seat of a new car" style="background:linear-gradient(135deg,#b7c0c8,#4e5a66)"></div>
      <h3>Car loans</h3>
      <p>We do not work for an insurance company, we work for you, we work on your side when you have a loss and follow through to see that you get often prompt payment. We represent a carefully selected group of reputable insurance companies.</p>
      <a class="btn">Read more</a>
    </article>
    <article class="loan">
      <div class="ph" role="img" aria-label="Family house with a green lawn" style="background:linear-gradient(180deg,#a9c4dc 0%,#c9b9a4 55%,#6f8b4d 100%)"></div>
      <h3>Home loans</h3>
      <p>We do not work for an insurance company, we work for you, we work on your side when you have a loss and follow through to see that you get often prompt payment. We represent a carefully selected group of reputable insurance companies.</p>
      <a class="btn">Read more</a>
    </article>
  </div>
</section>

<section class="about">
  <div class="about-main">
    <h2>What is Brook Ledger</h2>
    <h4>Wellcome to our business site</h4>
    <div class="ensure">
      <div class="ph" role="img" aria-label="Portrait of a smiling businesswoman" style="background:linear-gradient(180deg,#cfc6bf,#8d7e74)"></div>
      <div>
        <h5>We ensure</h5>
        <p>BrookLedger.com is the market leader in crowd lending/peer to peer lending in Ireland. Businesses/SME's can borrow anything from €5,000 to €100,000 at interest rates much more favourable than those offered by the banks.</p>
        <p>Our lenders are members of the public and they can lend directly to Irish businesses in amounts from €50 to €2,000. They get a better rate of return than deposit accounts, as well as the feel good factor of supporting a local business.</p>
      </div>
    </div>
  </div>
  <div class="video">
    <div class="video-info">
      <h5>Video title</h5>
      <p>Our lenders are members of the public and they can lend directly to Irish businesses in amounts from €50 to €2,000.</p>
      <p>They get a better rate of return than deposit accounts.</p>
      <svg width="40" height="12"><path d="M6 1L1 6l5 5" fill="none" stroke="#e2683c" stroke-width="2"/><path d="M30 1l5 5-5 5" fill="none" stroke="#e2683c" stroke-width="2"/></svg>
    </div>
    <div class="ph" role="img" aria-label="Video still of a hand drawing rising arrows" style="background:linear-gradient(135deg,#e9e9e9,#9a9a9a)">
      <svg width="290" height="170"><circle cx="145" cy="85" r="22" fill="rgba(0,0,0,.55)"/><polygon points="138,74 138,96 157,85" fill="#fff"/></svg>
    </div>
  </div>
  <aside class="faq">
    <h2>FAQ</h2>
    <ul>
      <li>We do not work for an company we work for you ?<small>we work on your side when you have a loss and follow through to see that you get often, prompt payment.</small></li>
      <li>We do not work for an company we work for you ?</li>
      <li>We do not work for an company we work for you ?</li>
      <li>We do not work for an company we work for you ?</li>
      <li>We do not work for an company we work for you ?</li>
      <li>We do not work for an company we work for you ?</li>
      <li>We do not work for an company we work for you ?</li>
      <li>We do not work for an company we work for you ?</li>
      <li>We do not work for an company we work for you ?</li>
      <li>We do not work for an company we work for you ?</li>
    </ul>
  </aside>
</section>

<section class="lend">
  <div class="ph" role="img" aria-label="Close-up of two business people shaking hands"></div>
  <h2>LOOKING TO LEND</h2>
  <p>To make a difference</p>
  <a class="btn">Get started now!</a>
  <svg class="arr" style="left:60px" width="16" height="28"><path d="M14 2L3 14l11 12" fill="none" stroke="#e2683c" stroke-width="3"/></svg>
  <svg class="arr" style="right:60px" width="16" height="28"><path d="M2 2l11 12L2 26" fill="none" stroke="#e2683c" stroke-width="3"/></svg>
</section>

<section class="news">
  <div class="ph bg" role="img" aria-label="Faint photo of a hand writing figures"></div>
  <div class="news-list">
    <h2>What is new</h2>
    <div class="prog"><b>1</b><div><h3>Program 1</h3><p>Please find information about our agency, its principles, and the various types of insurance coverage that we provide.</p></div></div>
    <div class="prog"><b>2</b><div><h3>Program 2</h3><p>Please find information about our agency, its principles, and the various types of insurance coverage that we provide.</p></div></div>
    <div class="prog"><b>3</b><div><h3>Program 3</h3><p>Please find information about our agency, its principles, and the various types of insurance coverage that we provide.</p></div></div>
  </div>
  <h2 class="calc-title">Loan Calculator</h2>
  <div class="calc">
    <div class="row"><label>Business Loan amount:</label><span class="val" style="margin-left:auto">€330.00</span></div>
    <div class="slider"><i style="left:60px"></i></div>
    <div class="row"><label>Monthly repayment:</label><span class="val" style="margin-left:auto">30 days</span></div>
    <div class="slider"><i style="left:60px"></i></div>
    <div class="row"><label style="width:auto">Total Repay:</label><span class="val">€330.00</span></div>
    <a class="apply">APPLY NOW</a>
  </div>
</section>

<footer class="footer">
  <div class="col">
    <h4>Navigation</h4>
    <ul><li>Home</li><li>Marketplace</li><li>FAQ</li><li>About us</li></ul>
  </div>
  <div class="col">
    <h4>Follow us</h4>
    <ul><li><i></i>Circlepage</li><li><i></i>Chirpline</li><li><i></i>RSS</li></ul>
  </div>
  <div class="col">
    <h4>Our location</h4>
    <p>Ireland Business<br>14 Quay Lane, Unit 3<br>Dunmore, D08 KX21<br><br>Phone: 01-555-0142<br>Fax: 01-555-0198</p>
  </div>
</footer>

</body>
</html>
```